Single page 8 1/2 x 11 flyer to entice new homeowners to visit our WEBSITE

A single page flyer that we can put on an easel that promotes our website, tallowpine58.com, to new homeowners for blinds, shades, bath hardware, cabinet organization, etc. This piece will be on an easel in sales centers, design studios and closing offices. We want the homeowners to know where they can go to get reliable products and service from a trusted partner of their builder for products that were not installed in their new home before they closed.

Enter the coupon code KQT10 to get 10% off of your entire purchase and free shipping. The product on our website will put the finishing touches on their home. ....make your house your home

Target Market(s)

New homebuyers

Industry/Entity Type

Residential Construction

Font styles to use
Serif

Colors
ec1f27

Requirements
Must have
• Logo and website, tallowpine58.com and tagline, make your house your home
Nice to have
• what will drive new homeowners to the website to purchase items they did not purchase before closing like window blinds and shades, bath hardware, ceiling fans, grills, electric fireplaces, etc.

```html
<!DOCTYPE html>
<html lang="en">
<head>
<meta charset="utf-8">
<title>Tallow Pine 58 – Make Your House Your Home</title>
<link rel="stylesheet" href="https://fonts.googleapis.com/css2?family=Josefin+Sans:wght@300;400;600&family=Open+Sans:ital,wght@0,600;0,800;1,800&display=swap">
<style>
  :root {
    --brand-red: #ec1f27;
    --deep-red: #d71920;
    --ink: #1a1a1a;
    --slate: #3a3f45;
    --paper: #ffffff;
    --backdrop: #eceae6;
    --tape: rgba(236, 190, 175, 0.75);
    --room-warm: #d9b88e;
    --room-light: #f1e6d6;
  }
  * { box-sizing: border-box; margin: 0; padding: 0; }
  html, body { width: 1200px; height: 1200px; overflow: hidden; }
  body {
    background: var(--backdrop);
    font-family: "Josefin Sans", sans-serif;
    color: var(--ink);
    position: relative;
  }
  .flyer {
    position: absolute;
    left: 152px; top: 20px;
    width: 896px; height: 1160px;
    background: var(--paper);
    overflow: hidden;
  }
  /* header */
  .brand {
    position: absolute; left: 52px; top: 66px;
    display: flex; align-items: center; gap: 14px;
  }
  .brand-dot {
    width: 52px; height: 52px; border-radius: 50%;
    background: var(--brand-red);
  }
  .brand-name {
    font-weight: 600; font-size: 38px; letter-spacing: 1px;
    color: var(--slate); line-height: 1; padding-top: 6px;
  }
  .contact-top {
    position: absolute; right: 50px; top: 78px;
    text-align: right; font-size: 27px; line-height: 34px;
    font-weight: 400;
  }
  .contact-top .phone { color: var(--brand-red); }
  .rule-red {
    position: absolute; left: 0; top: 190px; width: 100%; height: 11px;
    background: var(--brand-red);
  }
  /* hero */
  .hero-photo {
    position: absolute; left: 0; top: 201px; width: 100%; height: 489px;
    background:
      linear-gradient(90deg, rgba(255,255,255,0.82) 0%, rgba(255,255,255,0.55) 38%, rgba(255,255,255,0) 60%),
      linear-gradient(160deg, var(--room-light) 0%, var(--room-warm) 55%, #8a5a3c 100%);
  }
  .tagline {
    position: absolute; left: 61px; top: 222px;
    font-size: 72px; font-weight: 300; line-height: 70px;
    text-transform: uppercase; letter-spacing: -1px;
  }
  .tagline .red { color: var(--brand-red); }
  /* offer band */
  .offer-band {
    position: absolute; left: 0; top: 690px; width: 100%; height: 385px;
    background: var(--deep-red); color: var(--paper);
  }
  .offer-title {
    position: absolute; left: 60px; top: 58px;
    font-size: 62px; font-weight: 300; letter-spacing: -1px; line-height: 1;
    white-space: nowrap;
  }
  .offer-rule {
    position: absolute; left: 53px; top: 126px; width: 542px; height: 2px;
    background: var(--paper);
  }
  .offer-sub {
    position: absolute; left: 0; width: 660px; top: 146px;
    text-align: center; font-size: 25px; font-weight: 300; color: var(--ink);
  }
  .offer-copy {
    position: absolute; left: 60px; width: 540px; top: 180px;
    text-align: center; font-size: 15px; line-height: 18px; font-weight: 300;
  }
  .offer-copy p + p { margin-top: 15px; }
  .product-circle {
    position: absolute; left: 19px; top: 198px; width: 116px; height: 116px;
    border-radius: 50%; background: linear-gradient(145deg, #ffffff, #e4e4e4);
  }
  .tag-label {
    position: absolute; background: var(--deep-red); color: #fff;
    border: 2px solid #fff; font-size: 13px; padding: 3px 8px;
    white-space: nowrap; font-weight: 400;
  }
  .tag-bath { left: 32px; top: 298px; transform: rotate(-25deg); }
  .snapshot {
    position: absolute; left: 597px; top: 202px; width: 240px; height: 160px;
    transform: rotate(22deg); background: #fff; padding: 8px;
    box-shadow: 0 3px 8px rgba(0,0,0,0.3);
  }
  .snapshot-photo {
    width: 100%; height: 100%;
    background: linear-gradient(120deg, #f4f2ea 0%, #d8d6c8 60%, #8b7560 100%);
  }
  .tag-window { left: 14px; top: 98px; }
  .tape {
    position: absolute; width: 88px; height: 20px; background: var(--tape);
  }
  .tape-a { left: 588px; top: 182px; transform: rotate(-8deg); }
  .tape-b { left: 768px; top: 370px; transform: rotate(-12deg); }
  /* badge */
  .badge {
    position: absolute; left: 637px; top: 596px; width: 212px; height: 212px;
    border-radius: 50%; background: #fff;
    border: 5px solid var(--brand-red);
    box-shadow: 0 0 0 3px #fff;
    font-family: "Open Sans", sans-serif;
    overflow: hidden;
  }
  .badge-text {
    position: absolute; left: 21px; top: 34px; width: 160px;
    transform: rotate(15deg); text-align: center;
  }
  .badge-big {
    color: var(--brand-red); font-weight: 800; font-style: italic;
    font-size: 23px; line-height: 25px;
  }
  .badge-big.lg { font-size: 32px; line-height: 34px; }
  .badge-small { color: #6c6c6c; font-weight: 600; font-size: 17px; line-height: 19px; margin-top: 2px; }
  /* footer */
  .footer {
    position: absolute; left: 0; top: 1100px; width: 100%;
    text-align: center; font-size: 20px; line-height: 21px; font-weight: 300;
    color: var(--ink);
  }
</style>
</head>
<body>
<main class="flyer">
  <header>
    <div class="brand">
      <span class="brand-dot"></span>
      <span class="brand-name">TALLOW PINE 58</span>
    </div>
    <div class="contact-top">
      <div class="phone">(555) 014-2786</div>
      <div class="site">www.tallowpine58.com</div>
    </div>
  </header>
  <div class="rule-red"></div>

  <section class="hero">
    <div class="hero-photo" role="img" aria-label="Bright furnished living room with fireplace, beige sofa, red lamp and large windows"></div>
    <h1 class="tagline">
      <span class="red">Make</span><br>Your<br><span class="red">House</span><br>Your<br><span class="red">Home</span>
    </h1>
  </section>

  <section class="offer-band">
    <h2 class="offer-title">TALLOW PINE 58</h2>
    <div class="offer-rule"></div>
    <p class="offer-sub">10% OFF YOUR ENTIRE PURCHASE</p>
    <div class="offer-copy">
      <p>Your builder and their trusted suppliers have<br>partnered together to offer you this special opportunity.</p>
      <p>Go to www.tallowpine58.com and shop for<br>your window coverings, ceiling fans, cabinet and<br>closet organization, bath hardware and more.</p>
      <p>During Checkout, enter coupon code "KQT10" and get<br>a 10% discount on your entire purchase and free shipping.<br>The product on our website will put the finishing touches on their home.</p>
    </div>

    <div class="product-circle" role="img" aria-label="Chrome towel ring bath hardware"></div>
    <span class="tag-label tag-bath">Bath Hardware</span>

    <span class="tape tape-a"></span>
    <figure class="snapshot">
      <div class="snapshot-photo" role="img" aria-label="Room with white vertical window blinds"></div>
      <span class="tag-label tag-window">Window Coverings</span>
    </figure>
    <span class="tape tape-b"></span>
  </section>

  <aside class="badge">
    <div class="badge-text">
      <div class="badge-big lg">10% off</div>
      <div class="badge-big">your entire<br>purchase!</div>
      <div class="badge-small">use promo<br>code EX10</div>
    </div>
  </aside>

  <footer class="footer">
    <div>CALL US: (555) 014-2786</div>
    <div>Visit us online: www.tallowpine58.com</div>
  </footer>
</main>
</body>
</html>
```